Bright Meadow Counseling Business Card design with a visually interesting use of Space

I need business cards that are luxurious and give a peaceful, calm vibe. I also had some letterhead designed, and i like the look of it also, it's attached with the logo design for reference/ ideas but feel free to be creative.

Target Market(s)

High end luxurious client who needs counseling

Industry/Entity Type

Marriage and Family Therapy

Contact Information for Business Card

Mira Kowalczyk MS LMFT/ or Toby Hallett address 4150 Larkin Suite 600

Font styles to use
Sans Serif

Colors
0054AA
0677BA
7BADD7
CADEEF
E8F1F8
0094D4
00A9DD
6FCCEA
C7EBF8
E9F6FB
A7469A
B969AE
D3A5CF
EDDBEB
F8F0F9
6B429C
8869AF
B7A5CE
E3DAEB
F3F0F8

Requirements
Must have
• Logo and color scheme but be simple modern and luxurious
Nice to have
• I'd like to incorporate some elelmets from the logo and letterhead into a simple modern card

```html
<!DOCTYPE html>
<html lang="en">
<head>
<meta charset="utf-8">
<title>Bright Meadow Counseling – Business Card</title>
<link rel="stylesheet" href="https://fonts.googleapis.com/css2?family=Lato:wght@300;400&display=swap">
<style>
  :root {
    --page-bg: #d4d4d4;
    --card-dark: #000000;
    --card-light: #ffffff;
    --ink: #111111;
    --rule: #9a9a9a;
    --violet: #8869af;
    --mark: #6b429c;
    --icon-phone: #7a4fa6;
    --icon-mail: #4f9ed6;
    --icon-web: #b9609f;
  }
  * { box-sizing: border-box; margin: 0; padding: 0; }
  html, body {
    width: 1200px;
    height: 1200px;
    overflow: hidden;
    background: var(--page-bg);
    font-family: "Lato", sans-serif;
  }
  .card {
    position: absolute;
    top: 303px;
    width: 367px;
    height: 593px;
    overflow: hidden;
  }
  .card--front { left: 201px; background: var(--card-dark); }
  .card--back  { left: 599px; background: var(--card-light); }

  .card__wash {
    position: absolute;
    left: 0; top: 0;
    width: 367px;
    height: 260px;
    display: block;
  }

  .brand {
    position: absolute;
    left: 0; top: 0;
    width: 100%;
    height: 100%;
    font-weight: 300;
  }
  .brand__mark {
    position: absolute;
    left: 262px;
    top: 410px;
    width: 58px;
    height: 58px;
    border-radius: 50%;
    background: var(--mark);
  }
  .brand__text {
    position: absolute;
    right: 104px;
    top: 470px;
    color: #ffffff;
    text-align: right;
    line-height: 1;
  }
  .brand__name { display: block; font-size: 33px; font-weight: 300; letter-spacing: 0.5px; }
  .brand__sub  { display: block; font-size: 20px; font-weight: 300; letter-spacing: 3px; margin-top: 8px; }

  .contact {
    position: absolute;
    left: 0; right: 0;
    top: 363px;
    text-align: center;
    color: var(--ink);
  }
  .contact__name { font-size: 30px; font-weight: 400; line-height: 1; }
  .contact__icons {
    display: flex;
    align-items: center;
    justify-content: center;
    gap: 4px;
    margin-top: 22px;
  }
  .contact__line { width: 38px; height: 1px; background: var(--rule); margin: 0 4px; }
  .icon { width: 25px; height: 25px; display: block; }
  .contact__details {
    list-style: none;
    margin-top: 10px;
    font-size: 17px;
    line-height: 21.5px;
    letter-spacing: 0.3px;
  }
  .contact__rule { width: 164px; height: 1px; background: var(--rule); margin: 8px auto 0; }
  .contact__address { font-size: 17px; margin-top: 8px; }
</style>
</head>
<body>

<section class="card card--front">
  <svg class="card__wash" viewBox="0 0 367 260" role="img" aria-label="Decorative area in deep navy, plum and teal tones">
    <defs>
      <linearGradient id="wash-dark" x1="0" y1="0" x2="1" y2="0.4">
        <stop offset="0" stop-color="#0a2230"/>
        <stop offset="0.3" stop-color="#221028"/>
        <stop offset="0.6" stop-color="#180b22"/>
        <stop offset="1" stop-color="#2a0b22"/>
      </linearGradient>
    </defs>
    <path d="M0 0H367V215C330 240 285 250 240 248C170 245 120 200 60 195C30 193 12 190 0 186Z" fill="url(#wash-dark)"/>
  </svg>
  <div class="brand">
    <span class="brand__mark"></span>
    <h1 class="brand__text">
      <span class="brand__name">Bright Meadow</span>
      <span class="brand__sub">Counseling</span>
    </h1>
  </div>
</section>

<section class="card card--back">
  <svg class="card__wash" viewBox="0 0 367 260" role="img" aria-label="Decorative area in blue, violet, magenta and teal tones">
    <defs>
      <linearGradient id="wash-light" x1="0" y1="0" x2="1" y2="0.4">
        <stop offset="0" stop-color="#6fc4ea"/>
        <stop offset="0.25" stop-color="#b46ab2"/>
        <stop offset="0.55" stop-color="#9670b3"/>
        <stop offset="0.8" stop-color="#4f77c0"/>
        <stop offset="1" stop-color="#9c3a86"/>
      </linearGradient>
    </defs>
    <path d="M0 0H367V215C330 240 285 250 240 248C170 245 120 200 60 195C30 193 12 190 0 186Z" fill="url(#wash-light)"/>
  </svg>
  <div class="contact">
    <h2 class="contact__name">Toby Hallett</h2>
    <div class="contact__icons">
      <span class="contact__line"></span>
      <svg class="icon" viewBox="0 0 25 25" aria-label="Phone">
        <rect width="25" height="25" rx="2" fill="var(--icon-phone)"/>
        <path d="M6 10c0-3 13-3 13 0v1.5h-3V10h-7v1.5H6z" fill="#fff"/>
        <rect x="8" y="12" width="9" height="6" rx="1" fill="#fff"/>
      </svg>
      <svg class="icon" viewBox="0 0 25 25" aria-label="Email">
        <rect width="25" height="25" rx="2" fill="var(--icon-mail)"/>
        <rect x="5.5" y="8" width="14" height="10" fill="none" stroke="#fff" stroke-width="1.2"/>
        <path d="M5.5 8l7 5.5 7-5.5M5.5 18l5-4.5M19.5 18l-5-4.5" fill="none" stroke="#fff" stroke-width="1.2"/>
      </svg>
      <svg class="icon" viewBox="0 0 25 25" aria-label="Website">
        <rect width="25" height="25" rx="2" fill="var(--icon-web)"/>
        <circle cx="12.5" cy="12.5" r="7" fill="#fff"/>
        <path d="M9 9c2 0 3 1 2.5 3s-2 2-2.5 4M14 7.5c1 1.5 3 1.5 3.5 3s-1 3-2 4.5" fill="none" stroke="var(--icon-web)" stroke-width="1.6"/>
      </svg>
      <span class="contact__line"></span>
    </div>
    <ul class="contact__details">
      <li>5550142387</li>
      <li>hello@brightmeadow.com</li>
      <li>www.brightmeadow.com</li>
    </ul>
    <div class="contact__rule"></div>
    <p class="contact__address">4150 Larkin Suite 600</p>
  </div>
</section>

</body>
</html>
```